AUSTRALIA SUPPLEMENT - Protein label design - CREATIVE, FEMININE, UNIQUE

I need help with the design of what will be my line of supplements. (Protein, plant base, collagen , BCAAs, etc)
I'm starting off with protein isolate - with the flavours VANILLA, CHOCOLATE, BOYSENBERRY, HONEYCOMB.
I need help with the design of what the product will look like for my range.
(Great opportunity for further work)

Looking for a unique, elegant, stand out, feminine design, some slight sparkle or something that stands out on a shelf.
With symbols to represent what's in it, raised text. with some quirky cute things on it. (not sure what) Something that captured young womens eyes and easy to understand. things on it that appeals to women such as
LOW CALORIE, GREAT TASTING, GLUTEN FREE, 100 NATURAL, NATURALLY SWEETENED, HIGH PROTEIN.etc and whatever you can think of (open to ideas) but within PCF guidelines.

Mostly just after the look and creativity of what the front will look like. Don't have to worry about the back area.

My market will be for females aged 18-35

I have a activewear line called BRONTUK which will go with this. which I will attach the logo below amongst some other things that match my packaging. (again open to ideas)

I have attached a label of what one will look like( EXAMPLE).
. Among others that look nice But again I want to be different, unique to stand out. I don't want it to look like these. it's just the only ones I found online I liked that suit my market.

Feel free to ask any questions! :)
Updates

Extending time as I want this to be to be what will be on the shelves of many stores. I know that needs time to be able to do a quality job.

Target Market(s)

18-35

Industry/Entity Type

Supplement

Font styles to use
Serif
Script

Colors
f9d9e8
ffffff
fbd3d4
ecf7fb
e4daeb
cfeae6
eea4c8
fdfad7
f59195

Requirements
Must have
• Word - BRONTUK
PROTEIN ISOLATE
FLAVOUR
SYMBOLS

Looking for a unique, elegant, stand out, colour, feminine design, some slight sparkle or something that stands out on a shelf.

IT WILL BE ON A WHITE TUB or CLEAR - Perhaps detail on the lid
Nice to have
• Looking for a unique, elegant, stand out, colour, feminine design, some slight sparkle or something that stands out on a shelf. Something artsy.

will be on a white or clear tub with a white label background (possibly)
Should not have
• I don’t want it dark looking.
Something bright, vibrant, whites, pinks, sparkles (maybe) colours.

I don't want the word activewear on it.

```html
<!DOCTYPE html>
<html lang="en">
<head>
<meta charset="utf-8">
<title>BRONTUK Protein Isolate Vanilla Label</title>
<link href="https://fonts.googleapis.com/css2?family=Marcellus&display=swap" rel="stylesheet">
<style>
  :root {
    --paper: #ffffff;
    --plum: #8e2b80;
    --ink: #2a2430;
    --taupe: #6e5f66;
    --petal-pink: #ef8fb0;
    --petal-rose: #f59195;
    --petal-lilac: #b48ad6;
    --leaf: #6fa88a;
  }
  html, body {
    margin: 0;
    padding: 0;
    width: 1200px;
    height: 1200px;
    overflow: hidden;
    background: var(--paper);
  }
  .label {
    position: relative;
    width: 1200px;
    height: 1200px;
    font-family: "Marcellus", serif;
  }
  .label-art {
    position: absolute;
    inset: 0;
  }
  .label-text {
    position: absolute;
    left: 350px;
    width: 500px;
    top: 0;
    height: 1200px;
    text-align: center;
  }
  .brand-name {
    position: absolute;
    left: 0; right: 0;
    top: 455px;
    margin: 0;
    font-size: 64px;
    letter-spacing: 6px;
    color: var(--ink);
    font-weight: 400;
  }
  .product-type {
    position: absolute;
    left: 0; right: 0;
    top: 622px;
    margin: 0;
    font-size: 29px;
    color: var(--taupe);
    letter-spacing: 0.5px;
  }
  .flavour {
    position: absolute;
    left: 0; right: 0;
    top: 672px;
    margin: 0;
    font-size: 62px;
    color: var(--plum);
    letter-spacing: 1px;
    font-weight: 400;
  }
  .volume {
    position: absolute;
    left: 0; right: 0;
    top: 782px;
    margin: 0;
    font-size: 28px;
    color: var(--taupe);
  }
</style>
</head>
<body>
  <main class="label">
    <svg class="label-art" width="1200" height="1200" viewBox="0 0 1200 1200">
      <defs>
        <linearGradient id="wreath-tones" x1="0" y1="0" x2="1" y2="1">
          <stop offset="0" stop-color="#f3a6c6"/>
          <stop offset="0.35" stop-color="#f59195"/>
          <stop offset="0.6" stop-color="#c79ae0"/>
          <stop offset="1" stop-color="#ee9fc3"/>
        </linearGradient>
      </defs>
      <g class="side-panels" role="img" aria-label="Plum mandala pattern panels on both sides of the label">
        <path class="side-panel side-panel--left" d="M175 295 H350 V905 H175 Q155 905 155 885 V315 Q155 295 175 295 Z" fill="var(--plum)"/>
        <path class="side-panel side-panel--right" d="M850 295 H1025 Q1045 295 1045 315 V885 Q1045 905 1025 905 H850 Z" fill="var(--plum)"/>
      </g>
      <ellipse class="floral-wreath" role="img" aria-label="Watercolour wreath of pink and lilac flowers with line-drawn blossoms and leaves"
        cx="600" cy="600" rx="385" ry="465" fill="none" stroke="url(#wreath-tones)" stroke-width="105" opacity="0.82"/>
    </svg>
    <div class="label-text">
      <h1 class="brand-name">BRONTUK</h1>
      <p class="product-type">PROTEIN ISOLATE</p>
      <h2 class="flavour">VANILLA</h2>
      <p class="volume">250 ml</p>
    </div>
  </main>
</body>
</html>
```